Design some Business Cards

Create a set of business cards for council of Geodesy.
The cards should be somehow indicative of the level/ status age group of the members, which i why a small description of the stages is included.
The card should look professional and colours and designs should match or complement the initial scheme.

```html
<!DOCTYPE html>
<html lang="en">
<head>
<meta charset="utf-8">
<title>council of Geodesy – Business Cards</title>
<link href="https://fonts.googleapis.com/css2?family=Montserrat:wght@400;600;700&display=swap" rel="stylesheet">
<style>
  :root {
    --bg: #e6e8e6;
    --card: #ffffff;
    --card-back: #f6f6f4;
    --green: #6f8f3c;
    --green-light: #9cc14a;
    --ink: #2b2b2b;
    --muted: #555555;
    --rule: #b9c79a;
  }
  * { margin: 0; padding: 0; box-sizing: border-box; }
  html, body {
    width: 1200px; height: 900px; overflow: hidden;
    background: var(--bg);
    font-family: "Montserrat", Arial, sans-serif;
  }
  .sheet {
    width: 1200px; height: 900px;
    display: flex; align-items: center; justify-content: center; gap: 60px;
  }
  .card {
    width: 525px; height: 300px;
    box-shadow: 0 10px 30px rgba(0,0,0,0.15);
    position: relative;
  }
  /* Front */
  .card-front {
    background: var(--card);
    display: flex; align-items: center; justify-content: center; gap: 18px;
  }
  .brand-dot {
    width: 46px; height: 46px; border-radius: 50%;
    background: var(--green-light);
  }
  .brand-name {
    font-weight: 600; font-size: 30px; color: var(--green);
    line-height: 1.1;
  }
  /* Back */
  .card-back {
    background: var(--card-back);
    display: flex; align-items: center;
    padding: 0 34px;
  }
  .back-brand {
    width: 130px;
    display: flex; flex-direction: column; align-items: flex-start; gap: 10px;
  }
  .back-brand .brand-dot { width: 30px; height: 30px; }
  .back-brand .brand-name { font-size: 17px; }
  .divider {
    width: 1px; height: 190px; background: var(--rule);
    margin: 0 14px 0 10px;
  }
  .icon-column {
    display: flex; flex-direction: column; gap: 14px; margin-right: 16px;
    margin-top: 48px;
  }
  .icon-column svg { width: 16px; height: 16px; fill: var(--green); display: block; }
  .details { flex: 1; }
  .person-name {
    font-weight: 700; font-size: 18px; letter-spacing: 0.5px;
    color: var(--ink); text-transform: uppercase;
  }
  .person-role { font-size: 14px; color: var(--muted); margin: 2px 0 18px; }
  .contact-list { list-style: none; font-size: 12px; color: var(--muted); line-height: 1.55; }
  .contact-list .address { margin-top: 12px; }
</style>
</head>
<body>
<main class="sheet">
  <section class="card card-front">
    <span class="brand-dot"></span>
    <span class="brand-name">council<br>of Geodesy</span>
  </section>

  <section class="card card-back">
    <div class="back-brand">
      <span class="brand-dot"></span>
      <span class="brand-name">council<br>of Geodesy</span>
    </div>
    <span class="divider"></span>
    <div class="icon-column">
      <svg viewBox="0 0 24 24" aria-label="phone"><path d="M6.6 10.8a15.1 15.1 0 0 0 6.6 6.6l2.2-2.2a1 1 0 0 1 1-.25 11.4 11.4 0 0 0 3.6.57 1 1 0 0 1 1 1V20a1 1 0 0 1-1 1A17 17 0 0 1 3 4a1 1 0 0 1 1-1h3.5a1 1 0 0 1 1 1c0 1.25.2 2.45.57 3.6a1 1 0 0 1-.25 1z"/></svg>
      <svg viewBox="0 0 24 24" aria-label="email"><path d="M2 5h20v14H2z M4 7v.4l8 5 8-5V7l-8 5z" fill-rule="evenodd"/></svg>
      <svg viewBox="0 0 24 24" aria-label="web"><circle cx="12" cy="12" r="9" fill="none" stroke="#6f8f3c" stroke-width="2"/><path d="M3 12h18M12 3c3 3 3 15 0 18M12 3c-3 3-3 15 0 18" fill="none" stroke="#6f8f3c" stroke-width="1.6"/></svg>
      <svg viewBox="0 0 24 24" aria-label="location"><path d="M12 2a7 7 0 0 0-7 7c0 5.2 7 13 7 13s7-7.8 7-13a7 7 0 0 0-7-7zm0 9.5A2.5 2.5 0 1 1 12 6.5a2.5 2.5 0 0 1 0 5z"/></svg>
    </div>
    <div class="details">
      <h1 class="person-name">Rowan Hale</h1>
      <p class="person-role">Partner</p>
      <ul class="contact-list">
        <li>+61 400 555 010</li>
        <li>+61 7 3555 0199</li>
        <li>rowan@geodesycouncil.org</li>
        <li>www.geodesycouncil.org</li>
        <li class="address">PO Box 2281, Brisbane QLD 4000</li>
      </ul>
    </div>
  </section>
</main>
</body>
</html>
```